Energy trading company (Voltrisa) needs a business card

We need a business card for a company based in Central America. Our main purpose is trading energy . We already have the logo but we need some good creativity to design a high impact business card. Colors blue, orange, green can be used or we would like to see good combinatios with our logo

Target Market(s)

Energy

Industry/Entity Type

Power Generation

Contact Information for Business Card

Logo , headquarters , name, background

Font styles to use
Serif
Sans Serif

Colors

Designer to choose colors to be used in the design.

Requirements
Must have
• it must have a fresh and clean view
Nice to have
• good backgrounds that combine with the logo
Should not have
• too much words

```html
<!DOCTYPE html>
<html lang="en">
<head>
<meta charset="utf-8">
<title>Voltrisa Business Card</title>
<link href="https://fonts.googleapis.com/css2?family=Open+Sans:wght@400;600&display=swap" rel="stylesheet">
<style>
  :root {
    --bg: #d4d4d4;
    --orange: #ef8f21;
    --orange-deep: #b85f14;
    --orange-mid: #d47a1c;
    --orange-light: #f4a03a;
    --streak: #f2c48e;
    --ink: #2b2b2b;
    --paper: #ffffff;
    --paper-shade: #e6e6e6;
  }
  * { margin: 0; padding: 0; box-sizing: border-box; }
  html, body { width: 1200px; height: 900px; overflow: hidden; }
  body {
    background: var(--bg);
    font-family: "Open Sans", Arial, sans-serif;
    position: relative;
  }
  .card {
    position: absolute;
    left: 280px;
    width: 640px;
    height: 366px;
    box-shadow: 0 6px 14px rgba(0,0,0,0.25);
    overflow: hidden;
  }
  .card-back { top: 64px; }
  .card-front {
    top: 470px;
    background: linear-gradient(160deg, var(--paper-shade) 0%, var(--paper) 50%);
  }
  .back-base {
    position: absolute; inset: 0;
    background: linear-gradient(160deg, var(--orange-mid) 0%, var(--orange) 70%, var(--orange-light) 100%);
  }
  .back-emblem-zone {
    position: absolute;
    left: -60px; bottom: -40px;
    width: 380px; height: 300px;
    border-radius: 0 190px 0 0;
    background: linear-gradient(100deg, var(--orange-light) 0%, var(--orange-deep) 70%, var(--orange) 100%);
    opacity: 0.9;
  }
  .back-streak-zone {
    position: absolute;
    right: -80px; top: -120px;
    width: 520px; height: 420px;
    background: radial-gradient(ellipse at 70% 30%, rgba(242,196,142,0.55) 0%, rgba(242,196,142,0.2) 40%, rgba(242,196,142,0) 70%);
  }
  .brand-disc {
    position: absolute;
    right: 40px; top: 28px;
    width: 240px; height: 240px;
    border-radius: 50%;
    background: var(--orange);
  }
  .brand-name {
    position: absolute;
    left: 48px; top: 96px;
    color: var(--orange);
    font-size: 48px; font-weight: 400;
    letter-spacing: 1px;
    line-height: 1;
    text-transform: uppercase;
  }
  .person { position: absolute; left: 48px; top: 168px; }
  .person-name { color: var(--orange); font-size: 19px; font-weight: 400; line-height: 1.25; }
  .person-title { color: var(--ink); font-size: 15px; line-height: 1.3; }
  .address {
    position: absolute; left: 48px; top: 230px;
    color: var(--ink); font-size: 15px; line-height: 1.35; font-style: normal;
  }
  .contacts {
    position: absolute; left: 48px; top: 282px;
    list-style: none; color: var(--ink); font-size: 15px; line-height: 1.4;
  }
  .contacts li { display: flex; align-items: center; gap: 8px; }
  .contacts svg { width: 14px; height: 14px; flex: none; }
</style>
</head>
<body>
  <section class="card card-back" role="img" aria-label="Orange card back with a large decorative brand symbol in the lower left and fine radiating light streaks in the upper right">
    <div class="back-base"></div>
    <div class="back-streak-zone"></div>
    <div class="back-emblem-zone"></div>
  </section>

  <section class="card card-front">
    <span class="brand-disc"></span>
    <p class="brand-name">Voltrisa</p>
    <div class="person">
      <p class="person-name">Daniel Reyes</p>
      <p class="person-title">Founder</p>
    </div>
    <address class="address">
      48 Harbor Lane, Suite 210<br>
      Coral Bay, Florida, 33190
    </address>
    <ul class="contacts">
      <li>
        <svg viewBox="0 0 16 16" aria-hidden="true"><path fill="#ef8f21" d="M4 1l3 3-2 2c1 2 3 4 5 5l2-2 3 3-2 3C7 15 1 9 1 3z"/></svg>
        (555) 210-4837
      </li>
      <li>
        <svg viewBox="0 0 16 16" aria-hidden="true"><rect x="1" y="3" width="14" height="10" fill="none" stroke="#ef8f21" stroke-width="2"/><path d="M1 3l7 6 7-6" fill="none" stroke="#ef8f21" stroke-width="2"/></svg>
        daniel@voltrisa.com
      </li>
      <li>
        <svg viewBox="0 0 16 16" aria-hidden="true"><circle cx="8" cy="8" r="6.5" fill="none" stroke="#ef8f21" stroke-width="1.6"/><path d="M1.5 8h13M8 1.5c-3 3-3 10 0 13M8 1.5c3 3 3 10 0 13" fill="none" stroke="#ef8f21" stroke-width="1.2"/></svg>
        www.voltrisa.com
      </li>
    </ul>
  </section>
</body>
</html>
```